Jewellery Store Web design

We are looking at a redesign of an exclusive jewellery store. The idea of what we want is to display the type of jewellery we sell. Our main product range is white diamonds. We do not want people to buy online. This site will not display any prices but only display photos and the information about the store.
The client believes in the saying “A picture makes a thousand words” so this site needs to be more pictures – less words.
The website that the client loves is:
www.pelwickgems.com
The existing site can be found at:
http://www.lumarothevaults.com.au/
The site cannot be written in flash as the site must be viewable on Vexa/Talvo devices and will be implemented with our already designed CMS.
This project is only for the PSD file. We will code up the final submission ourselves.
Updates
Reason: We have some great designs and we have decided to gurrantee the project and for those who want a payment gurrantee to enter.
Target Market(s)
Young Couples, 30+
Industry/Entity Type
Store
Look and feel
Each slider illustrates characteristics of the customer's brand and the style your logo design should communicate.

```html
<!DOCTYPE html>
<html lang="en">
<head>
<meta charset="utf-8">
<title>Lumaro The Vaults – Perth Jewellers</title>
<link rel="stylesheet" href="https://fonts.googleapis.com/css2?family=Arimo:wght@400;700&family=Parisienne&display=swap">
<style>
  :root {
    --bg-dark: #1c1c1c;
    --ribbon-shade: #b9b9b9;
    --ink: #111111;
    --white: #ffffff;
    --muted: #7a7a7a;
    --footer-link: #555555;
    --tile-top: #5a5a5a;
    --tile-bottom: #2e2e2e;
    --gold: #c9a24a;
    --gold-deep: #8a6424;
    --silver: #d9d9d9;
    --silver-deep: #8d8d8d;
    --topaz: #2f8fa6;
  }
  * { box-sizing: border-box; margin: 0; padding: 0; }
  html, body { width: 1200px; height: 1000px; overflow: hidden; }
  body {
    position: relative;
    font-family: "Arimo", Arial, sans-serif;
    color: var(--white);
    background:
      radial-gradient(ellipse 600px 320px at 600px 280px, #5e5e5e 0%, #323232 60%, transparent 100%),
      repeating-linear-gradient(90deg, #262626 0 22px, #2a2a2a 22px 44px),
      var(--bg-dark);
  }
  .abs { position: absolute; }

  /* header ribbon */
  .ribbon { left: 112px; top: 56px; }
  .nav a {
    position: absolute; top: 85px; font-size: 13px; font-weight: 700;
    color: var(--ink); text-decoration: none;
  }
  .brand {
    left: 452px; top: 41px; width: 299px; height: 70px;
    background: #000; border: 2px solid #9a9a9a;
    display: flex; align-items: center; justify-content: center;
    font-size: 23px; font-weight: 400; letter-spacing: 1px; color: var(--white);
  }

  /* slider */
  .slider { left: 140px; top: 125px; width: 913px; height: 315px; background: #000; overflow: hidden; }
  .slide-panel { position: absolute; background: linear-gradient(#0b0b0b, #050505); }
  .slide-img { position: absolute; border-radius: 10px; }
  .caption { position: absolute; font-family: "Parisienne", cursive; color: #cfcfcf; white-space: nowrap; }
  .slide-left-panel { left: 48px; top: 80px; width: 155px; height: 160px; }
  .slide-left-img { left: 72px; top: 85px; width: 96px; height: 120px;
    background: linear-gradient(160deg, var(--gold) 0%, var(--topaz) 30%, #1d5d6e 55%, var(--gold) 80%, var(--gold-deep) 100%); }
  .slide-main-img { left: 358px; top: 42px; width: 185px; height: 160px; border-radius: 40px 60px 30px 30px;
    background: radial-gradient(ellipse at 65% 40%, #b08a5e 0%, #7a5a36 35%, #d5ab55 62%, #6a4a1e 100%); }
  .slide-right-panel { left: 715px; top: 100px; width: 143px; height: 145px; }
  .slide-right-img { left: 718px; top: 108px; width: 110px; height: 90px; border-radius: 45px;
    background: radial-gradient(ellipse at 55% 40%, #ffffff 0%, var(--silver) 35%, var(--silver-deep) 75%, #3a3a3a 100%); }
  .slider-curve { left: 0; top: 0; }
  .arrow { width: 29px; height: 29px; border-radius: 50%; background: radial-gradient(circle at 40% 35%, #666, #222); border: 2px solid #9a9a9a; }
  .dots { left: 533px; top: 433px; display: flex; gap: 9px; }
  .dots span { width: 11px; height: 11px; border-radius: 50%; background: #050505; }
  .dots span.active { background: #777; }

  .tagline {
    left: 112px; top: 465px; width: 976px; height: 37px; background: #242424;
    border-top: 1px solid #3a3a3a; border-bottom: 1px solid #3a3a3a;
    font-size: 12px; font-weight: 700; text-align: center; line-height: 35px;
  }

  /* category tiles */
  .tiles { left: 127px; top: 520px; width: 930px; height: 88px; display: flex; border-radius: 6px;
    background: linear-gradient(var(--tile-top), var(--tile-bottom)); }
  .tile { position: relative; border-right: 1px solid #222; }
  .tile:last-child { border-right: 0; }
  .tile-img { position: absolute; }
  .tile h3 { position: absolute; top: 29px; font-size: 12px; font-weight: 700; white-space: nowrap; }
  .tile p { position: absolute; top: 44px; font-size: 11px; font-weight: 700; color: var(--muted); }

  /* welcome */
  .welcome { left: 133px; top: 629px; width: 253px; }
  .welcome h2 { font-size: 15px; font-weight: 700; margin-bottom: 13px; }
  .welcome p { font-size: 11px; line-height: 18px; text-align: justify; margin-bottom: 18px; }

  .visit { left: 455px; top: 648px; }
  .visit h2 { font-size: 23px; font-weight: 700; }
  .visit p { font-size: 11px; font-weight: 700; margin: 3px 0 0 3px; }
  .thumb { position: absolute; top: 718px; width: 108px; height: 140px; border-radius: 6px;
    background:
      radial-gradient(ellipse 34px 30px at 58% 25%, #ffffff 0%, #c8c8c8 70%, transparent 72%),
      linear-gradient(150deg, #f3f3f3 0%, #e2e2e2 45%, var(--gold) 62%, #e6c774 78%, #f0f0f0 100%); }

  /* footer */
  .footer-rule { left: 127px; top: 890px; width: 950px; height: 1px; background: #3a3a3a; }
  .footer-nav a { position: absolute; top: 906px; font-size: 11px; font-weight: 700; color: var(--footer-link); text-decoration: none; }
  .join { left: 505px; top: 960px; font-size: 12px; font-weight: 700; color: #888; }
  .social { top: 955px; width: 24px; height: 24px; border-radius: 50%; background: #777; }
</style>
</head>
<body>

<svg class="abs ribbon" width="978" height="69" viewBox="0 0 978 69" aria-hidden="true">
  <defs>
    <linearGradient id="ribbonFill" x1="0" x2="1">
      <stop offset="0" stop-color="#ffffff"/>
      <stop offset="0.35" stop-color="#f0f0f0"/>
      <stop offset="0.7" stop-color="#e6e6e6"/>
      <stop offset="1" stop-color="#b9b9b9"/>
    </linearGradient>
  </defs>
  <polygon points="0,0 978,0 945,34 978,69 0,69 33,34" fill="url(#ribbonFill)"/>
  <polygon points="340,54 358,54 358,69" fill="#8a949a"/>
  <polygon points="619,54 637,54 619,69" fill="#8a949a"/>
</svg>
<nav class="nav">
  <a style="left:187px">Home</a>
  <a style="left:260px">About us</a>
  <a style="left:346px">Collection</a>
  <a style="left:797px">Diamonds</a>
  <a style="left:892px">Friends</a>
  <a style="left:972px">Contact</a>
</nav>
<div class="abs brand">LUMARO THE VAULTS</div>

<section class="abs slider">
  <div class="slide-panel slide-left-panel"></div>
  <div class="slide-img slide-left-img" role="img" aria-label="Gold earrings set with blue topaz"></div>
  <span class="caption" style="left:92px;top:210px;font-size:14px">Devero Mias</span>
  <div class="slide-img slide-main-img" role="img" aria-label="Gold cocktail ring with large smoky quartz and black and white diamonds"></div>
  <span class="caption" style="left:398px;top:240px;font-size:19px">Invecto Nasea</span>
  <div class="slide-panel slide-right-panel"></div>
  <div class="slide-img slide-right-img" role="img" aria-label="White gold filigree diamond ring"></div>
  <span class="caption" style="left:740px;top:218px;font-size:14px">Lorem Ipsum</span>
  <svg class="abs slider-curve" width="913" height="315" viewBox="0 0 913 315" aria-hidden="true">
    <path d="M0,315 L0,300 Q456,255 913,300 L913,315 Z" fill="#3a3a3a"/>
  </svg>
</section>
<div class="abs arrow" style="left:153px;top:256px"><svg width="25" height="25" viewBox="0 0 25 25"><path d="M14 8 L10 12.5 L14 17" stroke="#fff" stroke-width="2" fill="none"/></svg></div>
<div class="abs arrow" style="left:1012px;top:256px"><svg width="25" height="25" viewBox="0 0 25 25"><path d="M11 8 L15 12.5 L11 17" stroke="#fff" stroke-width="2" fill="none"/></svg></div>
<div class="abs dots"><span class="active"></span><span></span><span></span><span></span><span></span><span></span><span></span><span></span></div>

<div class="abs tagline">Perth Jewellers specialising in gold, diamonds and pearls</div>

<section class="abs tiles">
  <div class="tile" style="width:322px">
    <div class="tile-img" role="img" aria-label="Stack of diamond engagement rings" style="left:10px;top:-10px;width:120px;height:104px;border-radius:40px;background:radial-gradient(ellipse at 45% 40%,#ffffff 0%,var(--silver) 40%,var(--silver-deep) 80%,#555 100%)"></div>
    <h3 style="left:149px">LATEST COLLECTION</h3><p style="left:212px">VIEW MORE</p>
  </div>
  <div class="tile" style="width:307px">
    <div class="tile-img" role="img" aria-label="Diamond drop earrings" style="left:30px;top:-2px;width:68px;height:86px;border-radius:30px 30px 34px 34px;background:radial-gradient(ellipse at 50% 70%,#e8e8e8 0%,#b5b5b5 45%,#6a6a6a 80%,#444 100%)"></div>
    <h3 style="left:130px">DIAMOND JEWELLERY</h3><p style="left:199px">VIEW MORE</p>
  </div>
  <div class="tile" style="width:301px">
    <div class="tile-img" role="img" aria-label="Diamond clover pendant on a chain" style="left:28px;top:-4px;width:52px;height:92px;border-radius:18px 18px 26px 26px;background:radial-gradient(ellipse at 50% 75%,#ffffff 0%,var(--silver) 40%,#777 85%,#4a4a4a 100%)"></div>
    <h3 style="left:104px">GOLD AND SIVER COLLECTION</h3><p style="left:223px">VIEW MORE</p>
  </div>
</section>

<section class="abs welcome">
  <h2>Welcome to Lumaro The Vaults</h2>
  <p>Lumaro The Vaults is Perth's most recent jewellery boutique to open on Kelby Street, Perth WA specialising in rare diamonds and pearls jewellery.</p>
  <p>With an in-house designer, a team of qualified jewellers and setters located on the premises, Lumaro The Vaults design exclusive individual pieces, engagement and wedding rings.</p>
  <p>Lumaro The Vaults's quality pieces are everlasting and will be cherished beyond a life time.</p>
</section>

<section class="abs visit">
  <h2>Visit Lumaro The Vaults</h2>
  <p>if you would like to enquire about their diamond selection or in-house design service.</p>
</section>
<div class="thumb" style="left:459px" role="img" aria-label="Princess cut diamond ring in yellow gold"></div>
<div class="thumb" style="left:578px" role="img" aria-label="Princess cut diamond ring in yellow gold"></div>
<div class="thumb" style="left:700px" role="img" aria-label="Princess cut diamond ring in yellow gold"></div>
<div class="thumb" style="left:820px" role="img" aria-label="Princess cut diamond ring in yellow gold"></div>
<div class="thumb" style="left:937px" role="img" aria-label="Princess cut diamond ring in yellow gold"></div>

<div class="abs footer-rule"></div>
<nav class="footer-nav">
  <a style="left:354px">Home</a>
  <a style="left:421px">About us</a>
  <a style="left:499px">Collection</a>
  <a style="left:586px">Diamonds</a>
  <a style="left:673px">Friends</a>
  <a style="left:746px">Contact</a>
</nav>
<span class="abs join">JOIN US</span>
<svg class="abs" style="left:562px;top:960px" width="8" height="12" viewBox="0 0 8 12" aria-hidden="true"><path d="M1 1 L6 6 L1 11" stroke="#888" stroke-width="1.5" fill="none"/></svg>
<span class="abs social" style="left:580px" aria-label="Social network"></span>
<span class="abs social" style="left:619px" aria-label="Social network"></span>
<span class="abs social" style="left:657px" aria-label="Social network"></span>

</body>
</html>
```